Want to fly? Flight school needs a roll up

Hello designers

We are a small aviation club with around 100 members. We love flying and therefore offer free flight lessons for young people at our glider flight school.
The young people only have to pay a flat rate of €300 for the aircraft until their first solo flight.
To advertise the flight school we now need a roll up banner measuring 85cm x 200cm. You can find the data sheet for the banner in the appendix.
Content of the roll up banner:
Advertising for our flight school so that we can attract new members
The banner should be designed in our club colors blue/white
The banner is aimed at all people who want to get a glider license
A great offer for young people up to the age of 25 should be placed on the banner with a reference to the text “Offer only applies to people up to the age of 25. Included in the flat rate of €300 is training on the glider up to the first "solo flight"
The banner is intended to advertise training with a glider. Therefore the wish would be for a glider to be depicted

Here is a link to our current homepage

https://www.lsg-kornbach.de/

https://www.videohub-example.com/watch?v=Q8-t2Lp4xZn

Target Market(s)

Young people from 14 years to 30 years

Colors
0054AA
0677BA
7BADD7
CADEEF
E8F1F8

Requirements
Nice to have
• Glider / club logo
Should not have
• Too much text

```html
<!DOCTYPE html>
<html lang="de">
<head>
<meta charset="utf-8">
<title>Roll-up – Segelflugschule</title>
<link href="https://fonts.googleapis.com/css2?family=Saira+Condensed:ital,wght@0,700;1,600;1,700;1,800;1,900&display=swap" rel="stylesheet">
<style>
  :root{
    --club-blue:#2a52a5;
    --deep-blue:#0054aa;
    --mid-blue:#0677ba;
    --sky-blue:#7badd7;
    --pale-blue:#cadeef;
    --mist:#e8f1f8;
    --navy:#1f2f80;
    --white:#ffffff;
  }
  *{margin:0;padding:0;box-sizing:border-box}
  html,body{width:1200px;height:750px;overflow:hidden;background:var(--white)}
  body{position:relative;font-family:"Saira Condensed",sans-serif}
  .rollup{
    position:absolute;left:459px;top:43px;width:282px;height:664px;overflow:hidden;
    background:var(--club-blue);
  }
  .sky{
    position:absolute;left:0;top:0;width:282px;height:471px;
    background:linear-gradient(180deg,#2b55a6 0%,var(--deep-blue) 28%,#1266b6 55%,#3f8ccc 78%,var(--sky-blue) 90%,var(--pale-blue) 100%);
  }
  .club-mark{position:absolute;left:84px;top:34px;width:114px;height:114px}
  .club-name{
    position:absolute;left:0;top:153px;width:282px;text-align:center;
    font-style:italic;font-weight:700;font-size:13px;color:var(--white);letter-spacing:.3px;
  }
  .headline{position:absolute;left:0;top:0;width:282px;color:var(--white);font-style:italic;font-weight:900;text-shadow:0 2px 6px rgba(0,30,80,.35)}
  .headline .kicker{position:absolute;left:40px;top:178px;font-size:40px;line-height:1;letter-spacing:.5px}
  .headline .big{position:absolute;left:38px;font-size:118px;line-height:1;letter-spacing:-2px}
  .headline .pilot{top:206px}
  .headline .jetzt{top:300px;font-size:104px}
  .glider-photo{position:absolute;left:12px;top:262px;width:262px;height:72px}
  .offer-band{
    position:absolute;left:0;top:418px;width:282px;height:30px;
    background:linear-gradient(90deg,rgba(232,241,248,.2),rgba(232,241,248,.85) 20%,rgba(232,241,248,.85) 80%,rgba(232,241,248,.2));
    text-align:center;font-style:italic;font-weight:800;font-size:19px;line-height:30px;color:var(--navy);
  }
  .glider-icon{position:absolute;left:79px;top:484px;width:128px;height:24px}
  .terms-frame{position:absolute;left:30px;top:498px;width:224px;height:80px}
  .terms{
    position:absolute;left:50px;top:515px;width:184px;text-align:center;
    font-style:italic;font-weight:600;font-size:10.4px;line-height:12.8px;color:var(--white);
  }
  .contact{position:absolute;left:26px;top:595px;width:240px;color:var(--white);font-style:italic;font-weight:700;font-size:17px;line-height:20px}
  .contact li{list-style:none;display:flex;align-items:center;gap:5px;white-space:nowrap}
  .contact svg{width:17px;height:17px;flex:none}
</style>
</head>
<body>
<main class="rollup">
  <div class="sky" role="img" aria-label="Blauer Himmel mit hellen Schönwetterwolken"></div>

  <svg class="club-mark" viewBox="0 0 114 114" aria-hidden="true">
    <circle cx="57" cy="57" r="50" fill="none" stroke="#ffffff" stroke-width="3"/>
  </svg>
  <p class="club-name">Luftsportgruppe Kornbach e.V.</p>

  <h1 class="headline">
    <span class="kicker">Etwas Werden</span>
    <span class="big pilot">Pilot</span>
    <span class="big jetzt">Jetzt!</span>
  </h1>

  <svg class="glider-photo" viewBox="0 0 262 72" role="img" aria-label="Foto eines weißen Segelflugzeugs im Flug">
    <defs>
      <linearGradient id="gliderTone" x1="0" y1="0" x2="1" y2="1">
        <stop offset="0" stop-color="#e8f1f8" stop-opacity=".15"/>
        <stop offset=".5" stop-color="#e8f1f8" stop-opacity=".45"/>
        <stop offset="1" stop-color="#cadeef" stop-opacity=".15"/>
      </linearGradient>
    </defs>
    <rect width="262" height="72" rx="8" fill="url(#gliderTone)"/>
  </svg>

  <p class="offer-band">300 € bis zum ersten Alleinflug</p>

  <svg class="glider-icon" viewBox="0 0 128 24" role="img" aria-label="Segelflugzeug-Silhouette">
    <rect width="128" height="24" rx="4" fill="#7badd7" opacity=".75"/>
  </svg>
  <svg class="terms-frame" viewBox="0 0 224 80" aria-hidden="true">
    <path d="M26 2 H222 L214 66 Q212 78 198 78 H2 L12 16 Q14 2 26 2 Z" fill="none" stroke="#7badd7" stroke-width="1.2"/>
  </svg>
  <p class="terms">Das Angebot gilt nur für Personen bis zum vollendeten 25. Lebensjahr. In der Pauschale von 300 € ist die Ausbildung am Segelflugzeug bis zum ersten „Alleinflug“ enthalten.</p>

  <ul class="contact">
    <li>
      <svg viewBox="0 0 24 24" aria-hidden="true"><path d="M12 2a5 5 0 0 0-5 5c0 4 5 9 5 9s5-5 5-9a5 5 0 0 0-5-5zm0 7a2 2 0 1 1 0-4 2 2 0 0 1 0 4z" fill="#7badd7"/><path d="M3 22l3-7h3l3 3 3-3h3l3 7z" fill="#7badd7"/></svg>
      Postfach 34 20 • 72999 Kornbach
    </li>
    <li>
      <svg viewBox="0 0 24 24" aria-hidden="true"><path d="M6.6 10.8a15 15 0 0 0 6.6 6.6l2.2-2.2a1 1 0 0 1 1-.25 11.4 11.4 0 0 0 3.6.57 1 1 0 0 1 1 1V20a1 1 0 0 1-1 1A17 17 0 0 1 3 4a1 1 0 0 1 1-1h3.5a1 1 0 0 1 1 1c0 1.25.2 2.45.57 3.57a1 1 0 0 1-.25 1z" fill="#7badd7"/></svg>
      01234 / 5678 (Fluggelände Hohenfeld)
    </li>
  </ul>
</main>
</body>
</html>
```